Ebook cover needed for my Pagelit Crime Novel

My ebook takes place on a fictional island off the coast of Sydney, Australia. A 10 year old German boy, holidaying with his family, is found drowned just minutes after playing happily on a rope swing on a sunny day at Wren Creek. But an investigative journalist - and the boy's parents - think the police got it wrong. Is there a killer on the island? The cover must be bold, simple and the graphic image and print suitable for clear thumbprint viewing on Brightmart. The title is CHILD OF WREN CREEK and the author is MARGOT HASKELL. I'm looking for a stand-out cover that is designed to catch the reader's eye and is easy to read. I don't want a picture of a boy and would prefer something more abstract than literal.

Target Market(s)

Crime and thriller readers, women and men, all ages (adult)

Font styles to use
Serif
Sans Serif

Requirements
Must have
• A bold design, be evocative of murder without being too obvious (eg there is no blood or weapons because the boy drowns). The title needs to be around a third of the cover and my name should be as wide as the cover.
Nice to have
• These things are just thoughts, please don't feel you need to constrain your design ideas.
• A boy's hand on a tree. Some torn refill paper with handwriting in pen. A rope swing hanging from a tree. A river shot (narrow river not wide). Wilted flowers at the base of a tree. A finch (Australian bird) the river is named after - not necessarily a photo but a silhouette perhaps? A sense of the title being under water. A a blond boy's head from behind (just his hair).
Should not have
• A boy's face. Anything relating to a dark or stormy day or night - he disappears on a sunny day.

```html
<!DOCTYPE html>
<html lang="en">
<head>
<meta charset="UTF-8">
<title>Child of Wren Creek — Margot Haskell</title>
<link rel="stylesheet" href="https://fonts.googleapis.com/css2?family=Anton&family=Open+Sans:wght@400&display=swap">
<style>
  :root {
    --page-bg: #ffffff;
    --water-surface: #4a9fd6;
    --water-mid: #1c5fa8;
    --water-deep: #0b2f78;
    --water-floor: #0a2466;
    --title-ink: #a9b8d8;
    --author-ink: #ffffff;
  }
  * { margin: 0; padding: 0; box-sizing: border-box; }
  html, body {
    width: 1200px;
    height: 975px;
    overflow: hidden;
    background: var(--page-bg);
  }
  .stage {
    position: relative;
    width: 1200px;
    height: 975px;
  }
  .cover {
    position: absolute;
    left: 315px;
    top: 37px;
    width: 570px;
    height: 900px;
    overflow: hidden;
  }
  .cover-art {
    position: absolute;
    inset: 0;
    background:
      radial-gradient(ellipse 55% 18% at 50% 0%, rgba(190, 235, 255, 0.75), rgba(190, 235, 255, 0) 100%),
      linear-gradient(180deg, var(--water-surface) 0%, var(--water-mid) 22%, var(--water-deep) 55%, var(--water-floor) 100%);
  }
  .cover-title {
    position: absolute;
    left: 0;
    top: 0;
    width: 570px;
    height: 900px;
  }
  .cover-title text {
    font-family: "Anton", "Impact", sans-serif;
    fill: var(--title-ink);
    text-transform: uppercase;
  }
  .cover-author {
    position: absolute;
    left: 0;
    right: 0;
    top: 822px;
    text-align: center;
    font-family: "Open Sans", "Tahoma", sans-serif;
    font-weight: 400;
    font-size: 44px;
    letter-spacing: 1px;
    color: var(--author-ink);
  }
</style>
</head>
<body>
  <main class="stage">
    <article class="cover">
      <div class="cover-art" role="img" aria-label="Underwater view looking up toward a sunlit river surface, with a faint figure sinking among rising bubbles"></div>
      <svg class="cover-title" viewBox="0 0 570 900" aria-label="Child of Wren Creek">
        <text class="title-word" x="20" y="262" font-size="210" textLength="420" lengthAdjust="spacingAndGlyphs">CHILD</text>
        <text class="title-small" x="448" y="195" font-size="72" textLength="100" lengthAdjust="spacingAndGlyphs">OF</text>
        <text class="title-word" x="20" y="460" font-size="210" textLength="528" lengthAdjust="spacingAndGlyphs">WREN</text>
        <text class="title-word" x="20" y="660" font-size="210" textLength="528" lengthAdjust="spacingAndGlyphs">CREEK</text>
      </svg>
      <p class="cover-author">MARGOT HASKELL</p>
    </article>
  </main>
</body>
</html>
```